Email Signature

We are looking for creative email signature for our company. Please find attached the logo of our company for your reference. now we understand there isn't much can be done with email signature but we are looking for out of the box designs. Nothing specific in mind

Please insert fake numbers, website and/or address, etc just to showcase the designs. once the design is chosen we will provide the actual details.
Updates

Dear All,

We wouldlike to extend our apology for not being able to provide feedbacks to everysingle design. We were extremely busy and we have multiple contests opensimultaneously which makes the process harder. However, thank you all for theefforts you have put into this contest. We have received anoverwhelming quality responses & it has been a very difficult task tochoose just one, we easily Loved at least several designs...

Thanksagain for participating, we wish you all success in your design ventures.

Kindregards,

HLW Team

Industry/Entity Type

It Company

```html
<!DOCTYPE html>
<html lang="en">
<head>
<meta charset="utf-8">
<title>Harbor Lantern – Business Card</title>
<link rel="stylesheet" href="https://fonts.googleapis.com/css2?family=Ubuntu:ital,wght@0,400;0,500;0,700;1,400&display=swap">
<style>
  :root {
    --paper-light: #ececea;
    --paper-dark: #d4d5d0;
    --brand-blue: #2aa6e2;
    --band-blue: #0f80e0;
    --band-blue-deep: #0a6fd0;
    --band-glow: #9fd2f7;
    --text-white: #ffffff;
  }
  * { margin: 0; padding: 0; box-sizing: border-box; }
  html, body {
    width: 1200px;
    height: 683px;
    overflow: hidden;
    background: #ffffff;
  }
  .card {
    position: relative;
    width: 1200px;
    height: 683px;
    overflow: hidden;
    font-family: "Ubuntu", sans-serif;
  }
  .brand-band {
    position: absolute;
    left: 0;
    top: 0;
    width: 1200px;
    height: 313px;
    background: linear-gradient(160deg, var(--paper-light) 0%, #e2e3df 55%, var(--paper-dark) 100%);
    display: flex;
    align-items: center;
    padding-left: 40px;
  }
  .brand-name {
    font-family: "Ubuntu", sans-serif;
    font-weight: 700;
    font-size: 118px;
    line-height: 1;
    letter-spacing: -2px;
    color: var(--brand-blue);
    white-space: nowrap;
  }
  .contact-band {
    position: absolute;
    left: 0;
    top: 313px;
    width: 1200px;
    height: 370px;
  }
  .contact-band .backdrop {
    position: absolute;
    inset: 0;
    width: 100%;
    height: 100%;
  }
  .contact {
    position: absolute;
    left: 32px;
    top: 0;
    color: var(--text-white);
  }
  .contact .person-name {
    position: absolute;
    top: 26px;
    font-weight: 700;
    font-size: 68px;
    white-space: nowrap;
    line-height: 1;
  }
  .contact .position {
    position: absolute;
    top: 110px;
    font-style: italic;
    font-weight: 400;
    font-size: 47px;
    line-height: 1;
    white-space: nowrap;
  }
  .contact .line {
    position: absolute;
    font-size: 42px;
    font-weight: 400;
    line-height: 1;
    white-space: nowrap;
  }
  .contact .mobile { top: 183px; }
  .contact .fax { top: 242px; }
  .contact .email { top: 303px; }
</style>
</head>
<body>
  <div class="card">
    <header class="brand-band">
      <span class="brand-name">Harbor Lantern</span>
    </header>

    <section class="contact-band">
      <svg class="backdrop" viewBox="0 0 1200 370" preserveAspectRatio="none" role="img" aria-label="Abstract blue background with soft sweeping light streaks">
        <defs>
          <linearGradient id="bandBase" x1="0" y1="0" x2="1" y2="1">
            <stop offset="0" stop-color="var(--band-blue)"/>
            <stop offset="1" stop-color="var(--band-blue-deep)"/>
          </linearGradient>
          <radialGradient id="bandGlow" cx="0.82" cy="0.7" r="0.45">
            <stop offset="0" stop-color="var(--band-glow)" stop-opacity="0.75"/>
            <stop offset="1" stop-color="var(--band-glow)" stop-opacity="0"/>
          </radialGradient>
        </defs>
        <rect width="1200" height="370" fill="url(#bandBase)"/>
        <rect width="1200" height="370" fill="url(#bandGlow)"/>
      </svg>

      <div class="contact">
        <h1 class="person-name">Name Surname</h1>
        <p class="position">position</p>
        <p class="line mobile">m. 0491 570 156</p>
        <p class="line fax">Fax&nbsp; (03) 5550 4321</p>
        <p class="line email">email yourname@harborlantern.com</p>
      </div>
    </section>
  </div>
</body>
</html>
```